Bref créative
Stationery - Business Card / Letterhead
For Public Adjusting Company
Professional
Doran T. Whitcombe
Sr. Public Adjuster
58 W. Alder St.
Suite 612
Smithtown, NY 11492
doran@trclaimpro.com
www.trclaimpro.com
On the front I want our logo with the shadow on the bottom
On the back I would like you to incorporate a little creative usage of either the shield/lighthouse logo and all of my information
This logo should be used as the front as it has the bottom shadow which for some reason is not showing up on the other logos
the business card front will be high gloss finish
Also the fax number should be 516.843.9075 not 829. there is no where else for me to edit that once the project is uploaded

```html
<!DOCTYPE html>
<html lang="en">
<head>
<meta charset="utf-8">
<title>TR Claim Advisors – Stationery</title>
<link href="https://fonts.googleapis.com/css2?family=Cinzel:wght@600&family=Open+Sans:wght@400;600&display=swap" rel="stylesheet">
<style>
  :root{
    --navy:#1b3a66;
    --navy-deep:#0f2444;
    --navy-light:#2f5a92;
    --paper:#ffffff;
    --ink:#3b4350;
    --muted:#7a8290;
    --rule:#c9d3e1;
    --stage:#e7e9ec;
  }
  *{box-sizing:border-box;margin:0;padding:0}
  html,body{width:1200px;height:1002px;overflow:hidden}
  body{background:var(--stage);position:relative;font-family:"Open Sans",Arial,sans-serif;color:var(--ink)}
  .sheet{position:absolute;background:var(--paper);box-shadow:0 6px 18px rgba(20,30,50,.18)}

  .brand{display:flex;align-items:center;gap:10px}
  .brand-mark{width:22px;height:22px;background:var(--navy);flex:none}
  .brand-name{font-family:"Cinzel",Georgia,serif;font-weight:600;color:var(--navy);letter-spacing:.06em;line-height:1.05;text-transform:uppercase}

  /* Envelope */
  .envelope{left:40px;top:80px;width:420px;height:200px;padding:22px 24px}
  .envelope .brand-name{font-size:15px}
  .envelope .return{margin-top:8px;font-size:8px;color:var(--muted);padding-left:32px}
  .envelope .edge{position:absolute;left:0;right:0;bottom:0;height:6px;background:linear-gradient(90deg,var(--navy-deep),var(--navy-light))}

  /* Business card back */
  .card-back{left:40px;top:320px;width:420px;height:240px;border-radius:14px;padding:30px 30px}
  .card-back .brand-name{font-size:17px}
  .card-back .rule{height:1px;background:var(--rule);margin:16px 0 18px}
  .card-back .cols{display:flex;justify-content:space-between}
  .person .name{font-size:14px;font-weight:600;color:var(--navy)}
  .person .title{font-size:10px;color:var(--muted);margin-top:2px}
  .person .addr{font-size:10px;line-height:1.5;margin-top:18px}
  .contact{font-size:10px;line-height:1.7;text-align:left}
  .contact b{font-weight:600;color:var(--navy);display:inline-block;width:28px}

  /* Business card front */
  .card-front{left:40px;top:600px;width:420px;height:240px;border-radius:14px;
    background:radial-gradient(ellipse at 40% 30%,var(--navy-light),var(--navy) 55%,var(--navy-deep));
    display:flex;align-items:center;justify-content:center}
  .card-front .brand-mark{background:#fff;width:26px;height:26px}
  .card-front .brand-name{color:#fff;font-size:22px}
  .card-front .gloss{position:absolute;inset:0;border-radius:14px;background:linear-gradient(160deg,rgba(255,255,255,.18),rgba(255,255,255,0) 45%)}

  /* Letterhead */
  .letterhead{left:500px;top:60px;width:660px;height:880px;padding:44px 48px}
  .letterhead .brand-name{font-size:20px}
  .letterhead .brand-mark{width:28px;height:28px}
  .letterhead .head-rule{margin-top:18px;height:2px;background:linear-gradient(90deg,var(--navy),var(--navy-light) 60%,rgba(47,90,146,0))}
  .letterhead .footer{position:absolute;left:48px;right:48px;bottom:40px;text-align:center;font-size:9px;color:var(--muted);line-height:1.7}
  .letterhead .footer-rule{height:1px;background:var(--navy);margin-bottom:10px}
</style>
</head>
<body>

<section class="sheet envelope">
  <div class="brand"><span class="brand-mark"></span><span class="brand-name">TR Claim Advisors</span></div>
  <p class="return">58 W. Alder St. · Suite 612 · Smithtown, NY 11492</p>
  <div class="edge"></div>
</section>

<section class="sheet card-back">
  <div class="brand"><span class="brand-mark"></span><span class="brand-name">TR Claim Advisors</span></div>
  <div class="rule"></div>
  <div class="cols">
    <div class="person">
      <p class="name">Doran T. Whitcombe</p>
      <p class="title">Sr. Public Adjuster</p>
      <p class="addr">58 W. Alder St.<br>Suite 612<br>Smithtown, NY 11492</p>
    </div>
    <div class="contact">
      <p><b>Tel</b>516.843.9829</p>
      <p><b>Fax</b>516.843.9075</p>
      <p><b>Cell</b>516.843.9830</p>
      <p>doran@trclaimpro.com</p>
      <p>www.trclaimpro.com</p>
    </div>
  </div>
</section>

<section class="sheet card-front">
  <div class="brand"><span class="brand-mark"></span><span class="brand-name">TR Claim Advisors</span></div>
  <div class="gloss"></div>
</section>

<section class="sheet letterhead">
  <div class="brand"><span class="brand-mark"></span><span class="brand-name">TR Claim Advisors</span></div>
  <div class="head-rule"></div>
  <div class="footer">
    <div class="footer-rule"></div>
    <p>58 W. Alder St. · Suite 612 · Smithtown, NY 11492</p>
    <p>Tel 516.843.9829 · Fax 516.843.9075 · doran@trclaimpro.com · www.trclaimpro.com</p>
  </div>
</section>

</body>
</html>
```